Bref créative
Quorel Stationary
Stationary and Business Cards
I need double sided standard sized Business Card [3.5" x 2"]
show me your ideas
Corporate
Marcus Toddin
Chief Executive Officer
Halvenor Business Tower
18th Floor
PO Box 58217
Dubai
United Arab Emirates
mt@quorel.co
www.quorel.co
Show me your ideas

```html
<!DOCTYPE html>
<html lang="en">
<head>
<meta charset="utf-8">
<title>Quorel Stationary</title>
<link href="https://fonts.googleapis.com/css2?family=Open+Sans:wght@400;600&display=swap" rel="stylesheet">
<style>
:root{
  --blue:#1e9ad8;
  --blue-pale:#d4ecf8;
  --blue-faint:#e4f2fa;
  --ink:#3a3a3a;
  --muted:#7a7a7a;
  --paper:#ffffff;
  --stage:#e8e5df;
  --line:#9a9a9a;
}
*{box-sizing:border-box;margin:0;padding:0}
html,body{width:1200px;height:562px;overflow:hidden}
body{background:var(--stage);font-family:"Open Sans",Arial,sans-serif;color:var(--ink);position:relative}
.piece-wrap{position:absolute}
.piece{position:absolute;inset:0;background:var(--paper);box-shadow:0 2px 6px rgba(0,0,0,.25);overflow:hidden}
.piece-label{position:absolute;font-size:8px;font-weight:600;color:#333;text-align:center;width:100%;top:-13px;white-space:nowrap}
.swoosh{position:absolute;inset:0;width:100%;height:100%}
.brand-name{position:absolute;color:var(--blue);font-weight:600;line-height:1;white-space:nowrap}
.brand-watermark{position:absolute;color:var(--blue-faint);font-weight:400;line-height:1;white-space:nowrap}
.footer-line{position:absolute;bottom:14px;left:18px;right:40px;font-size:4.6px;color:var(--muted);text-align:center;white-space:nowrap}

/* fax */
.fax-title{position:absolute;top:50px;right:44px;font-size:8px;font-weight:600}
.fax-table{position:absolute;top:62px;left:18px;width:290px;border-collapse:collapse;font-size:6px}
.fax-table td{border:1px solid var(--line);height:17px;padding:0 3px}
.fax-table td.key{width:34px}
.fax-checks{position:absolute;top:140px;left:18px;display:flex;gap:14px;font-size:5.5px;white-space:nowrap}
.fax-checks span::before{content:"";display:inline-block;width:6px;height:6px;border:1px solid var(--line);margin-right:3px;vertical-align:-1px}

/* card */
.card-text{position:absolute;font-size:4.6px;line-height:1.5;color:var(--ink);white-space:nowrap}

/* signature */
.sig-address{position:absolute;left:104px;top:48px;font-size:6px;line-height:1.55;white-space:nowrap}
.sig-name{position:absolute;left:270px;top:64px;white-space:nowrap}
.sig-name strong{display:block;color:var(--blue);font-size:13px;font-weight:400}
.sig-name span{font-size:7px;font-weight:600}
</style>
</head>
<body>

<!-- Fax cover -->
<div class="piece-wrap" style="left:36px;top:26px;width:341px;height:516px">
  <div class="piece-label">Fax Cover</div>
  <div class="piece">
    <svg class="swoosh" viewBox="0 0 341 516" preserveAspectRatio="none" aria-hidden="true">
      <path d="M318 0 H341 V516 H300 C330 420 336 250 318 0 Z" fill="var(--blue)"/>
      <path d="M310 0 H318 C336 250 330 420 300 516 H292 C322 420 328 250 310 0 Z" fill="var(--blue-pale)"/>
    </svg>
    <div class="brand-name" style="left:146px;top:14px;font-size:9px">Quorel</div>
    <div class="fax-title">FAX</div>
    <table class="fax-table">
      <tr><td class="key">To:</td><td></td><td class="key">From:</td><td></td></tr>
      <tr><td class="key">Fax:</td><td></td><td class="key">Pages:</td><td></td></tr>
      <tr><td class="key">Phone:</td><td></td><td class="key">Date:</td><td></td></tr>
      <tr><td class="key">Re:</td><td></td><td class="key">CC:</td><td></td></tr>
    </table>
    <div class="fax-checks"><span>Urgent</span><span>For Review</span><span>Please Comment</span><span>Please Reply</span><span>Please Recycle</span></div>
    <div class="brand-watermark" style="left:95px;top:290px;font-size:40px">Quorel</div>
    <div class="footer-line">Halvenor Business Tower, 18th Floor, PO Box 58217, Dubai, United Arab Emirates · mt@quorel.co · www.quorel.co</div>
  </div>
</div>

<!-- Letterhead -->
<div class="piece-wrap" style="left:396px;top:26px;width:350px;height:516px">
  <div class="piece-label">Letterhead</div>
  <div class="piece">
    <svg class="swoosh" viewBox="0 0 350 516" preserveAspectRatio="none" aria-hidden="true">
      <path d="M326 0 H350 V516 H308 C340 420 344 250 326 0 Z" fill="var(--blue)"/>
      <path d="M318 0 H326 C344 250 340 420 308 516 H300 C332 420 336 250 318 0 Z" fill="var(--blue-pale)"/>
    </svg>
    <div class="brand-name" style="left:150px;top:16px;font-size:9px">Quorel</div>
    <div class="brand-watermark" style="left:100px;top:270px;font-size:40px">Quorel</div>
    <div class="footer-line">Halvenor Business Tower, 18th Floor, PO Box 58217, Dubai, United Arab Emirates · mt@quorel.co · www.quorel.co</div>
  </div>
</div>

<!-- Business card front -->
<div class="piece-wrap" style="left:763px;top:30px;width:137px;height:85px">
  <div class="piece-label">Business Card (Front)</div>
  <div class="piece">
    <svg class="swoosh" viewBox="0 0 137 85" preserveAspectRatio="none" aria-hidden="true">
      <path d="M0 62 C40 78 95 80 137 60 V85 H0 Z" fill="var(--blue)"/>
    </svg>
    <div class="brand-name" style="left:10px;top:22px;font-size:8px">Quorel</div>
    <div class="card-text" style="left:54px;top:12px"><b>Marcus Toddin</b><br>Chief Executive Officer<br>Halvenor Business Tower<br>PO Box 58217, Dubai<br>mt@quorel.co</div>
  </div>
</div>

<!-- Business card back -->
<div class="piece-wrap" style="left:912px;top:30px;width:139px;height:85px">
  <div class="piece-label">Business Card (Back)</div>
  <div class="piece">
    <svg class="swoosh" viewBox="0 0 139 85" preserveAspectRatio="none" aria-hidden="true">
      <path d="M0 50 C45 70 100 72 139 48 V85 H0 Z" fill="var(--blue)"/>
    </svg>
    <div class="brand-name" style="left:12px;top:20px;font-size:10px">Quorel</div>
    <div class="card-text" style="left:62px;top:24px;font-size:6px;color:var(--blue)">www.quorel.co</div>
  </div>
</div>

<!-- E-mail signature -->
<div class="piece-wrap" style="left:763px;top:144px;width:401px;height:144px">
  <div class="piece-label">E-Mail Signature</div>
  <div class="piece">
    <svg class="swoosh" viewBox="0 0 401 144" preserveAspectRatio="none" aria-hidden="true">
      <path d="M0 0 H30 C44 50 44 100 30 144 H0 Z" fill="var(--blue)"/>
    </svg>
    <div class="brand-name" style="left:46px;top:64px;font-size:14px">Quorel</div>
    <div class="sig-address">Halvenor Business Tower<br>18th Floor<br>PO Box 58217<br>Dubai<br>United Arab Emirates<br>mt@quorel.co<br>www.quorel.co</div>
    <div class="sig-name"><strong>Marcus Toddin</strong><span>Chief Executive Officer</span></div>
  </div>
</div>

<!-- Envelope -->
<div class="piece-wrap" style="left:763px;top:312px;width:401px;height:228px">
  <div class="piece-label">Envelope (Front)</div>
  <div class="piece">
    <svg class="swoosh" viewBox="0 0 401 228" preserveAspectRatio="none" aria-hidden="true">
      <path d="M0 150 C120 200 280 210 401 140 V228 H0 Z" fill="var(--blue)"/>
      <path d="M0 140 C120 190 280 200 401 130 V140 C280 210 120 200 0 150 Z" fill="var(--blue-pale)"/>
    </svg>
    <div class="brand-name" style="left:18px;top:20px;font-size:10px">Quorel</div>
  </div>
</div>

</body>
</html>
```